Website for Hash Orbita a cyrpto Mining company that sells crypto mining rigs

β€œIn the age of de-centralised financial services, individuals with a relatively small investment can use their own hardware to process crypto transactions and earn a substantial second income.”

Hash Orbita provide a personal home and hosted mining solutions to enable individuals to earn monthly crypto currencies of today and the future.”
Home/Products/About
Images – I had assumed this was part of the Design? For the home page I have a 10 second video of blockchain. I can only find on Pixelvault For any text or sections please refer to our old website www.thirdheron.ae
https://www.pixelvaultmedia.com/video/clip-2947163058-block-chain-concept---consists-network-connections I can buy and send?
On each page I will have a video similar, can you just put placeholder images and videos. I can replace. I am pretty good with Wordpress.
Updates

Please use text from my old website www.thirdheronmining.com

Target Market(s)

High Net wealth interested in Crypto

Industry/Entity Type

Crypto Mining

Coding

Coded - Design and coding required

Number of Pages Required

5+ page

Font styles to use
Other font styles liked:
• Sansation

Colors
0054AA
0677BA
7BADD7
CADEEF
E8F1F8

Requirements
Must have
• Video as banner (Will supply Video), Wordpress
Nice to have
• Will need Member login and Shop in future, please ensure this will be possible. (But not part of this project)

```html
<!DOCTYPE html>
<html lang="en">
<head>
<meta charset="utf-8">
<title>Hash Orbita — Third Heron Mining</title>
<link href="https://fonts.googleapis.com/css2?family=Exo+2:ital,wght@0,300;0,400;0,500;0,600;0,700;1,400&family=Montserrat:ital,wght@0,400;0,500;0,600;0,700;1,400&display=swap" rel="stylesheet">
<style>
:root{
  --navy:#121633;
  --navy-deep:#0d1026;
  --blue:#0054AA;
  --blue-mid:#0677BA;
  --blue-soft:#7BADD7;
  --blue-pale:#CADEEF;
  --blue-mist:#E8F1F8;
  --accent:#1aa3e8;
  --ink:#222;
  --grey:#777;
  --footer:#0c3f86;
  --footer-deep:#0a3571;
}
*{box-sizing:border-box;margin:0;padding:0}
html,body{width:1200px;height:5038px;overflow:hidden}
body{position:relative;font-family:"Montserrat",sans-serif;color:var(--ink);background:#fff}
.abs{position:absolute}
.heading{font-family:"Exo 2",sans-serif;font-weight:400;letter-spacing:.5px}
.heading b{font-weight:700;color:var(--blue-mid)}

/* nav + hero */
.hero{position:absolute;left:0;top:0;width:1200px;height:723px;background:radial-gradient(ellipse at 55% 45%,#1c2450 0%,var(--navy) 55%,var(--navy-deep) 100%)}
.hero-media{position:absolute;left:0;top:110px;width:940px;height:480px;background:radial-gradient(ellipse at 62% 50%,rgba(30,130,230,.75) 0%,rgba(20,80,180,.4) 35%,rgba(18,22,51,0) 70%)}
.nav{position:absolute;left:0;top:0;width:1200px;height:75px;background:rgba(10,12,30,.55);border-bottom:1px solid rgba(255,255,255,.06)}
.brand{position:absolute;left:121px;top:22px;display:flex;align-items:center;gap:12px}
.brand-dot{width:30px;height:30px;border-radius:50%;background:var(--accent)}
.brand-name{font-family:"Exo 2",sans-serif;font-weight:600;font-size:22px;color:var(--accent);letter-spacing:2px}
.nav-link{position:absolute;top:32px;font-size:11.5px;color:#fff;letter-spacing:.4px}
.nav-link.active{color:var(--accent)}
.nav-underline{position:absolute;left:340px;top:73px;width:88px;height:2px;background:var(--accent)}
.nav-login{position:absolute;left:938px;top:23px;width:129px;height:34px;background:var(--accent);color:#fff;font-size:10.5px;font-weight:700;display:flex;align-items:center;justify-content:center;letter-spacing:.4px}
.play-ring{position:absolute;left:557px;top:186px;width:86px;height:86px;border-radius:50%;background:rgba(10,12,30,.75)}
.hero-title{position:absolute;left:0;top:272px;width:1188px;text-align:center;font-family:"Exo 2",sans-serif;font-size:55px;color:#fff;font-weight:400;letter-spacing:1px}
.hero-title b{font-weight:700}
.hero-sub{position:absolute;left:0;top:342px;width:1188px;text-align:center;font-family:"Exo 2",sans-serif;font-weight:700;font-size:21px;line-height:27px;color:#fff}
.pill{position:absolute;left:524px;top:416px;width:164px;height:45px;border-radius:23px;background:#fff;color:var(--blue-mid);font-size:12.5px;font-weight:700;display:flex;align-items:center;justify-content:center;letter-spacing:.5px}

/* about */
.about-frame{position:absolute;left:94px;top:840px;width:156px;height:137px;border:3px solid var(--blue-mid);border-right:none;border-bottom:none}
.about-frame-side{position:absolute;left:94px;top:840px;width:3px;height:137px}
.about-block{position:absolute;left:450px;top:1079px;width:164px;height:123px;background:var(--blue)}
.about-photo{position:absolute;left:107px;top:854px;width:495px;height:329px;background:radial-gradient(ellipse at 55% 45%,#1f8a8a 0%,#0f3d45 45%,#081d24 100%)}
.about-play{position:absolute;left:107px;top:1140px;width:65px;height:43px;background:var(--blue-mid);display:flex;align-items:center;justify-content:center}
.eyebrow{font-size:14px;letter-spacing:2px;color:var(--blue-mid)}
.about-text{position:absolute;left:659px;top:858px;width:460px}
.about-text h2{font-size:44px;margin-top:4px}
.about-lead{margin-top:18px;font-size:15.5px;line-height:22px;color:var(--blue-mid)}
.about-body{margin-top:12px;font-size:12.5px;line-height:18px;color:var(--grey)}
.outline-btn{position:absolute;left:657px;top:1147px;width:162px;height:42px;border:2px solid var(--blue-mid);border-radius:21px;color:var(--blue-mid);font-size:12px;font-weight:700;display:flex;align-items:center;justify-content:center;letter-spacing:.5px}

/* services */
.services{position:absolute;left:0;top:1335px;width:1200px;height:780px;background:linear-gradient(135deg,#0a3d86 0%,#0d4fa8 45%,#0a3a80 100%)}
.services-art{position:absolute;left:560px;top:0;width:640px;height:780px;background:radial-gradient(ellipse at 70% 55%,rgba(60,150,230,.35) 0%,rgba(10,60,140,0) 70%)}
.section-label{position:absolute;left:0;width:1200px;text-align:center;color:#fff}
.card{position:absolute;background:#fff;padding:0 40px}
.card h3{font-size:15px;font-weight:600;color:#222;margin-top:0}
.card p{font-size:11px;line-height:17px;color:#888;margin-top:10px}
.card.featured{background:linear-gradient(160deg,#0a7fd6 0%,#0060b8 100%)}
.card.featured h3{color:#fff}
.card.featured p{color:#e5f0fa}
.card svg{display:block;margin-bottom:12px}

/* team */
.team-photo{position:absolute;width:209px;height:203px;border:3px solid var(--blue-mid);padding:6px;background:#fff}
.team-photo div{width:100%;height:100%;background:linear-gradient(180deg,#dfe6ee 0%,#9fb0c4 100%)}
.team-name{position:absolute;width:300px;text-align:center;font-family:"Exo 2",sans-serif;font-weight:700;font-size:18px;color:var(--blue-mid);line-height:21px}
.team-role{position:absolute;width:300px;text-align:center;font-size:12px;line-height:19px;color:#555}

/* testimonial */
.testimonial{position:absolute;left:0;top:2703px;width:1200px;height:649px;background:linear-gradient(180deg,#0a46a8 0%,#1c6fd4 55%,#0c4fb0 100%)}
.quote-photo{position:absolute;left:143px;top:2848px;width:453px;height:387px;background:linear-gradient(135deg,#0a1f55 0%,#1e5fbf 50%,#a9c9ff 100%)}
.quote-card{position:absolute;left:596px;top:2848px;width:454px;height:387px;background:#f1f1f1}
.quote-text{position:absolute;left:653px;top:2942px;width:350px;font-style:italic;font-size:11.5px;line-height:24px;color:#444}
.quote-author{position:absolute;left:655px;top:3122px;font-size:13px;color:#333}

/* faq */
.faq{position:absolute;left:182px;width:856px;border:2px solid var(--blue-soft);background:#fff}
.faq-q{position:absolute;left:28px;font-size:11.5px;font-weight:600;color:#333}
.faq-a{position:absolute;left:28px;top:52px;width:790px;font-size:11.5px;line-height:19px;color:#555}
.chev{position:absolute;right:16px}

/* contact */
.contact{position:absolute;left:0;top:4046px;width:1200px;height:598px;background:linear-gradient(180deg,#d5e7f6 0%,var(--blue-pale) 100%)}
.contact-panel{position:absolute;left:135px;top:4190px;width:340px;height:277px;background:linear-gradient(135deg,#0b4aa6 0%,#1976d2 60%,#2a8be0 100%)}
.form-card{position:absolute;left:475px;top:4166px;width:561px;height:379px;background:#fff;box-shadow:0 8px 24px rgba(0,60,140,.08)}
.field{position:absolute;border:1px solid #c8c8c8;font-size:11px;color:#666;padding:12px 14px}
.send{position:absolute;left:522px;top:4451px;width:162px;height:38px;background:var(--blue-mid);color:#fff;font-size:11px;font-weight:700;display:flex;align-items:center;justify-content:center;letter-spacing:.5px}

/* footer */
.footer{position:absolute;left:0;top:4644px;width:1200px;height:394px;background:var(--footer)}
.footer-base{position:absolute;left:0;top:4968px;width:1200px;height:70px;background:var(--footer-deep)}
.foot-rule{position:absolute;top:4702px;width:3px;height:25px;background:#fff}
.foot-head{position:absolute;top:4705px;font-size:12.5px;color:#fff;font-weight:500;letter-spacing:.4px}
.foot-label{position:absolute;font-size:10px;color:#9db9e0}
.foot-value{position:absolute;font-size:11.5px;color:#fff}
.foot-link{position:absolute;left:741px;font-size:10.5px;color:#fff}
.social{position:absolute;left:930px;display:flex;align-items:center;gap:14px;font-size:10.5px;color:#fff}
.social span.sq{width:18px;height:18px;background:#fff;display:inline-block}
</style>
</head>
<body>

<!-- Hero with video banner -->
<section class="hero">
  <div class="hero-media" role="img" aria-label="Video banner placeholder: glowing blue blockchain cube with binary digits"></div>
  <header class="nav">
    <div class="brand"><span class="brand-dot"></span><span class="brand-name">HASH ORBITA</span></div>
    <span class="nav-link active" style="left:350px">ABOUT US</span>
    <span class="nav-link" style="left:462px">SERVICES</span>
    <span class="nav-link" style="left:573px">FAQ</span>
    <span class="nav-link" style="left:647px">WHY US?</span>
    <span class="nav-link" style="left:755px">SHOP</span>
    <span class="nav-link" style="left:840px">CONTACT</span>
    <span class="nav-underline"></span>
    <span class="nav-login">MEMBER LOGIN</span>
  </header>
  <div class="play-ring"></div>
  <svg class="abs" style="left:586px;top:211px" width="30" height="36" viewBox="0 0 30 36"><path d="M4 3 L27 18 L4 33 Z" fill="none" stroke="#fff" stroke-width="3" stroke-linejoin="round"/></svg>
  <h1 class="hero-title">THIRD HERON <b>MINING</b></h1>
  <p class="hero-sub">THE EARLY BIRD GETS THE WORM, BUT THE THIRD<br>HERON GETS THE FISH</p>
  <span class="pill">GET STARTED</span>
</section>

<!-- About -->
<section aria-label="About">
  <div class="about-frame"></div>
  <div class="abs" style="left:94px;top:840px;width:3px;height:137px;background:var(--blue-mid)"></div>
  <div class="about-block"></div>
  <div class="about-photo" role="img" aria-label="Photo: glowing crypto coin symbol over a circuit board"></div>
  <div class="about-play"><svg width="20" height="22" viewBox="0 0 20 22"><path d="M2 1 L19 11 L2 21 Z" fill="#fff"/></svg></div>
  <div class="about-text">
    <p class="eyebrow">WHO WE ARE</p>
    <h2 class="heading">ABOUT <b>HASH ORBITA</b></h2>
    <p class="about-lead">IT and Operations since 2000, Digital Payments since 2007, Crypto since 2012.</p>
    <p class="about-body">Marcus and Liam were part of the core team that built Paylume.com. Liam has been running IT and Operation teams of large companies for many years before setting up his own IT and Security Consultancy.</p>
    <p class="about-body">Together this team know how to build, run and scale technology in Crypto and Payments, we only make 10% of your profits</p>
  </div>
  <span class="outline-btn">LEARN MORE</span>
</section>

<!-- Services -->
<section class="services">
  <div class="services-art" role="img" aria-label="Background art: blue network of connected nodes"></div>
  <p class="section-label" style="top:74px;font-size:13px;letter-spacing:2px">OUR SERVICES</p>
  <h2 class="section-label heading" style="top:92px;font-size:38px;color:#fff">WHAT <b style="color:#fff">WE DO</b></h2>
</section>

<div class="card" style="left:143px;top:1533px;width:303px;height:232px;padding-top:36px">
  <svg width="56" height="56" viewBox="0 0 56 56" fill="none" stroke="var(--blue-mid)" stroke-width="2"><rect x="14" y="14" width="28" height="28"/><circle cx="28" cy="28" r="7"/><path d="M20 14V6M28 14V6M36 14V6M20 42v8M28 42v8M36 42v8M14 20H6M14 28H6M14 36H6M42 20h8M42 28h8M42 36h8"/></svg>
  <h3>Hardware Installation</h3>
  <p>In the last few years, the technology required to 'mine' crypto has fallen significantly and the speed and ability</p>
</div>
<div class="card featured" style="left:446px;top:1529px;width:318px;height:243px;padding-top:36px">
  <svg width="60" height="58" viewBox="0 0 60 58" fill="none" stroke="#fff" stroke-width="2"><path d="M8 10 Q26 0 44 12"/><path d="M26 8 L8 48"/><circle cx="42" cy="40" r="11"/><path d="M42 33v14M38 36h6a2 2 0 0 1 0 4h-6h7a2 2 0 0 1 0 4h-7"/></svg>
  <h3>Currency Mining</h3>
  <p>Our typical "Quartz" rig contains 6 high powered gaming cards (GPUs) that produce amazing processing capabil-</p>
</div>
<div class="card" style="left:764px;top:1533px;width:305px;height:232px;padding-top:36px">
  <svg width="58" height="58" viewBox="0 0 58 58" fill="none" stroke="var(--blue-mid)" stroke-width="2"><circle cx="12" cy="12" r="9"/><circle cx="29" cy="12" r="9"/><circle cx="46" cy="12" r="9"/><circle cx="29" cy="29" r="9"/><circle cx="12" cy="46" r="9"/><circle cx="29" cy="46" r="9"/><circle cx="46" cy="46" r="9"/></svg>
  <h3>Crypto Earnings</h3>
  <p>With 50,000 AED invested, the Third Heron mining rig returns up to 0.4 AET per month.</p>
</div>
<div class="card" style="left:143px;top:1765px;width:303px;height:231px;padding-top:30px;border-top:1px solid #eee">
  <svg width="56" height="52" viewBox="0 0 56 52" fill="none" stroke="var(--blue-mid)" stroke-width="2"><rect x="4" y="8" width="48" height="40" rx="3"/><path d="M4 18h48M16 3v9M40 3v9"/><path d="M14 26h4M26 26h4M38 26h4M14 36h4M26 36h4M38 36h4"/></svg>
  <h3>Earn Crypto Every Month</h3>
  <p>When you become a Third Heron mining member, we help you open a CoinHarbor or Ledgerly Crypto account</p>
</div>
<div class="card" style="left:451px;top:1765px;width:308px;height:231px;padding-top:30px;border-top:1px solid #eee">
  <svg width="56" height="52" viewBox="0 0 56 52" fill="none" stroke="var(--blue-mid)" stroke-width="2"><circle cx="26" cy="26" r="15"/><circle cx="26" cy="26" r="22" stroke-dasharray="6 5"/><path d="M19 26l5 5 9-10"/></svg>
  <h3>Service &amp; Maintenance</h3>
  <p>The Third Heron service and mainte-nance team guarantee 96% platform up time, 24/7 customer service and same day</p>
</div>
<div class="card" style="left:764px;top:1765px;width:305px;height:231px;padding-top:30px;border-top:1px solid #eee">
  <svg width="56" height="54" viewBox="0 0 56 54" fill="none" stroke="var(--blue-mid)" stroke-width="2"><circle cx="27" cy="27" r="24"/><circle cx="27" cy="27" r="18"/><path d="M12 27h30M27 12v30"/></svg>
  <h3>Flexible Mining</h3>
  <p>Our Rig design means that you can choose to mine any cryptocurrency, not just Aethra.</p>
</div>

<!-- Team -->
<section aria-label="Team">
  <h2 class="section-label heading" style="top:2174px;font-size:36px;color:#222">MEET OUR <b>TEAM</b></h2>
  <div class="team-photo" style="left:188px;top:2287px"><div role="img" aria-label="Portrait photo of co-founder Marcus Hale"></div></div>
  <div class="team-photo" style="left:500px;top:2287px"><div role="img" aria-label="Portrait photo of co-founder Liam Carver"></div></div>
  <div class="team-photo" style="left:811px;top:2287px"><div role="img" aria-label="Photo of the technology and operations team at work"></div></div>
  <p class="team-name" style="left:142px;top:2517px">MARCUS HALE</p>
  <p class="team-role" style="left:142px;top:2545px">Co-Founder who operates the busi-<br>ness licenses, accounts and financial<br>service partnerships.</p>
  <p class="team-name" style="left:454px;top:2517px">LIAM CARVER</p>
  <p class="team-role" style="left:454px;top:2545px">Co-Founder who designs, builds and<br>maintains our hardware and software<br>solutions.</p>
  <p class="team-name" style="left:766px;top:2517px">PETAR &amp; NIKOLA<br>VAREL</p>
  <p class="team-role" style="left:766px;top:2567px">Our Technology and Operations gurus<br>who track the crypto markets daily.<br>Their remote access to the Third Heron<br>Mining rigs ensure they are optimised.</p>
</section>

<!-- Testimonial -->
<section class="testimonial">
  <h2 class="section-label heading" style="top:55px;font-size:33px;color:#fff">WHAT <b style="color:#fff">CLIENT SAYS</b></h2>
</section>
<div class="abs" style="left:129px;top:2835px;width:120px;height:110px;border-left:5px solid #fff;border-top:5px solid #fff"></div>
<div class="quote-photo" role="img" aria-label="Image: glowing blue data blocks with binary digits"></div>
<div class="quote-card"></div>
<div class="abs" style="left:958px;top:3161px;width:107px;height:84px;border-right:3px solid #fff;border-bottom:3px solid #fff"></div>
<svg class="abs" style="left:640px;top:2906px" width="40" height="30" viewBox="0 0 40 30"><path d="M2 28V14Q2 3 14 1v6Q8 8 8 14h7v14ZM22 28V14Q22 3 34 1v6Q28 8 28 14h7v14Z" fill="#d4d4d4"/></svg>
<p class="quote-text">"I had 10 thousands pounds saved but going nowhere. Liam explained that could buy a mining rig so I decided to invest it in the hardware. He came around himself, took about 2 hours to set it up, showed me how to open a CoinHarbor account and how to check the daily performance on my mobile or laptop. I can't quite believe it's making me money for what looks like nothing."</p>
<svg class="abs" style="left:888px;top:3090px" width="40" height="30" viewBox="0 0 40 30"><path d="M38 2v14Q38 27 26 29v-6Q32 22 32 16h-7V2ZM18 2v14Q18 27 6 29v-6Q12 22 12 16H5V2Z" fill="#d4d4d4"/></svg>
<p class="quote-author"><b>Canadian Pilot,</b> Falcon Skyways</p>

<!-- FAQ -->
<section aria-label="Frequently asked questions">
  <p class="section-label" style="top:3405px;font-size:16px;letter-spacing:1px;color:var(--blue-mid)">FAQ</p>
  <h2 class="section-label heading" style="top:3427px;font-size:31px;color:#222">FREQUENTLY <b>ASKED QUESTIONS</b></h2>

  <div class="faq" style="top:3519px;height:137px">
    <p class="faq-q" style="top:20px">What do I need to support a Home Mining rig?</p>
    <svg class="chev" style="top:18px" width="20" height="12" viewBox="0 0 20 12"><path d="M2 10l8-8 8 8" fill="none" stroke="var(--blue-mid)" stroke-width="2"/></svg>
    <p class="faq-a">You need just three things; 240W standard electricity power, broadband internet for which we recommend a minimum of 30 mps which standard Telvora and Netra broadband packages in UAE provide and a room or space which would ideally be kept below 23C temperature. The hardware will come fully installed in a standalone unit. The rig stands 90cm long, 50cm high, 35cm dee</p>
  </div>
  <div class="faq" style="top:3671px;height:47px"><p class="faq-q" style="top:14px">Would you like us to Host your Rig, potentially multiple Rigs in your own dedicated data centre?</p><svg class="chev" style="top:16px" width="20" height="12" viewBox="0 0 20 12"><path d="M2 2l8 8 8-8" fill="none" stroke="var(--blue-mid)" stroke-width="2"/></svg></div>
  <div class="faq" style="top:3730px;height:47px"><p class="faq-q" style="top:14px">Isn't Crypto Mining really bad for the planet?</p><svg class="chev" style="top:16px" width="20" height="12" viewBox="0 0 20 12"><path d="M2 2l8 8 8-8" fill="none" stroke="var(--blue-mid)" stroke-width="2"/></svg></div>
  <div class="faq" style="top:3789px;height:49px"><p class="faq-q" style="top:15px">EIP 1559?&nbsp; The reduction of gas fees to stay competitive and reduce supply.</p><svg class="chev" style="top:17px" width="20" height="12" viewBox="0 0 20 12"><path d="M2 2l8 8 8-8" fill="none" stroke="var(--blue-mid)" stroke-width="2"/></svg></div>
  <div class="faq" style="top:3849px;height:47px"><p class="faq-q" style="top:14px">What is The Flippening?</p><svg class="chev" style="top:16px" width="20" height="12" viewBox="0 0 20 12"><path d="M2 2l8 8 8-8" fill="none" stroke="var(--blue-mid)" stroke-width="2"/></svg></div>
  <div class="faq" style="top:3908px;height:49px"><p class="faq-q" style="top:15px">What is the difference between Proof of Work and Proof of Stake?</p><svg class="chev" style="top:17px" width="20" height="12" viewBox="0 0 20 12"><path d="M2 2l8 8 8-8" fill="none" stroke="var(--blue-mid)" stroke-width="2"/></svg></div>
</section>

<!-- Contact -->
<section class="contact" aria-label="Contact"></section>
<div class="abs" style="left:121px;top:4176px;width:140px;height:110px;border-left:3px solid #fff;border-top:3px solid #fff"></div>
<div class="abs" style="left:731px;top:4141px;width:329px;height:130px;border-right:3px solid var(--blue);border-top:3px solid var(--blue)"></div>
<div class="contact-panel" role="img" aria-label="Image: blue digital data blocks"></div>
<p class="abs" style="left:178px;top:4214px;font-size:12px;color:#fff;letter-spacing:1px">CONTACT US <span style="display:inline-block;width:30px;height:1px;background:#fff;vertical-align:middle;margin-left:6px"></span></p>
<p class="abs heading" style="left:178px;top:4238px;font-size:28px;line-height:30px;color:#fff">REQUEST A<br><b style="color:#fff">QUOTE &amp;<br>CONSULTATION</b></p>
<div class="form-card"></div>
<div class="field" style="left:520px;top:4221px;width:223px;height:43px">First Name</div>
<div class="field" style="left:755px;top:4221px;width:224px;height:43px">Last Name</div>
<div class="field" style="left:520px;top:4279px;width:223px;height:43px">Email address</div>
<div class="field" style="left:755px;top:4279px;width:224px;height:43px">Phone</div>
<div class="field" style="left:520px;top:4336px;width:459px;height:98px">Leave message</div>
<span class="send">SEND MESSAGE</span>

<!-- Footer -->
<footer class="footer"></footer>
<div class="footer-base"></div>
<div class="abs" style="left:195px;top:4736px;width:100px;height:100px;border-radius:50%;border:4px solid #fff"></div>
<p class="abs" style="left:120px;top:4834px;width:250px;text-align:center;font-family:'Exo 2',sans-serif;font-weight:600;font-size:26px;color:#fff;letter-spacing:3px">HASH ORBITA</p>

<span class="foot-rule" style="left:414px"></span>
<p class="foot-head" style="left:452px">CONTACT US</p>
<svg class="abs" style="left:455px;top:4742px" width="26" height="26" viewBox="0 0 26 26"><path d="M6 2l4 5-3 3q3 6 9 9l3-3 5 4-3 4Q12 24 2 6Z" fill="none" stroke="#fff" stroke-width="1.6" stroke-linejoin="round"/></svg>
<p class="foot-label" style="left:506px;top:4740px">Phone Number</p>
<p class="foot-value" style="left:506px;top:4758px">+971 50 000 1234</p>
<svg class="abs" style="left:455px;top:4803px" width="28" height="22" viewBox="0 0 28 22"><rect x="1" y="1" width="26" height="20" fill="none" stroke="#fff" stroke-width="1.6"/><path d="M1 1l13 11L27 1" fill="none" stroke="#fff" stroke-width="1.6"/></svg>
<p class="foot-label" style="left:506px;top:4800px">Email address</p>
<p class="foot-value" style="left:506px;top:4818px">liam@hashorbita.ae</p>
<svg class="abs" style="left:458px;top:4856px" width="22" height="30" viewBox="0 0 22 30"><path d="M11 29Q1 16 1 11a10 10 0 0 1 20 0q0 5-10 18Z" fill="none" stroke="#fff" stroke-width="1.6"/><circle cx="11" cy="11" r="4" fill="none" stroke="#fff" stroke-width="1.6"/></svg>
<p class="foot-label" style="left:506px;top:4857px">Office address</p>
<p class="foot-value" style="left:506px;top:4876px">Dubai, United Arab Emirates</p>

<span class="foot-rule" style="left:696px"></span>
<p class="foot-head" style="left:741px">NAVIGATION</p>
<p class="foot-link" style="top:4739px">ABOUT US</p>
<p class="foot-link" style="top:4765px">FAQ</p>
<p class="foot-link" style="top:4791px">WHY US</p>
<p class="foot-link" style="top:4817px">SERVICES</p>
<p class="foot-link" style="top:4843px">CONTACT US</p>
<p class="foot-link" style="top:4869px">SHOP</p>

<span class="foot-rule" style="left:899px"></span>
<p class="foot-head" style="left:930px">GET IN TOUCH</p>
<p class="social" style="top:4741px"><span class="sq"></span>FRIENDPAGE</p>
<p class="social" style="top:4778px"><span class="sq"></span>CHIRPLINE</p>
<p class="social" style="top:4814px"><span class="sq"></span>LINKWORK</p>

<p class="abs" style="left:0;top:4989px;width:1200px;text-align:center;font-size:10px;color:#fff">Copyright 2021 HashOrbita.com All Right Reserved</p>

</body>
</html>
```